Cruise Booking Website

Cruise search and booking website

This project is a redesign of a cruise booking website we did a few years ago.

The current website is located here: http://voyage.pixelmarsh.com/en/

It's not fully functional but gives you ad idea how miserable the old design was.

All the information about cruises, cruise lines, destinations, ports and shore excursions will be similar to http://www.sailorbay.com/
Actual search pages (form, results, single result, sailing and cabin selection, ship info, booking) will have EXACTLY the same info as sailorbay.com

We like the style of http://harborvoyagehub.com, it's quite modern, good spacing, not overloaded with information. So you can use it as an example of what we like, not what we want as a final result for us. Please, don't copy it. The result should not be possible to resemble the harborvoyagehub.com, because our site has to be unique. This is important!
If you submit a design that clearly reminds another cruise site it will be rejected!

Also the mockup provided is just to give you the basic structure and show what information has to be present on the page. It doesn't mean the layout has to be the same as a mockup. The layout is up to the designer.

I've updated the mockup to be more generic so it doesn't confuse you:
https://www.filecrate.net/s/k7q2mz9pw4tnb3x/Home%20page.png

When you're adding social sharing icons like chatterbox/peeplet you have to use chinese ones instead:
https://www.filecrate.net/s/h3rt8wyd6jcl0fe/chinese-social-icons.png
Originals: http://shrtlk.example/qRmT

We'll start with home page first and after it's approved inner pages can be designed.

I know the cost of the project doesn't look high, but the task is straight forward and doesn't require to be very original, it's better to follow existing design and layout patterns that proved to work well.
That's why I encourage you to choose a template to build the design on top of one of https://themequarry.net/ themes if it will save the design work, will be easier and faster for you. So it will be more like a customization than a new design from scratch.

Mockups, site map and logo files:
- https://www.filecrate.net/sh/50xb7vq1ndtpkez/RmwuHp8Zq3

Website tree:
- https://papers.quillnet.example/document/d/8vTrXk2MqLpZ4wNsB7yHcE1oUjFgD9aR_QbVtnWm/edit?usp=sharing
Updates

So far a lot of designs are just copying http://www.harborvoyagehub.com/ - we don't like it!

We like the style of harborvoyagehub.com, it's quite modern, good spacing, not overloaded with information. So you can use it as an example of what we like, not what we want as a final result for us. Please, don't copy it. The result should not be possible to resemble the harborvoyagehub.com, because our site has to be unique. This is important!

Target Market(s)

Chinese travellers

Industry/Entity Type

Build

Requirements
Must have
• * White, blue and red
* Large spacing, not too much information cramped into a small space like sailorbay.com or the current website
* More "hidden" info in popups, tabs and so on, so not to many things are visible at the same time
* Compatible with lumen framekit styling (for easier coding):
- http://lumenkit.example.io/framework/index.html
- http://skinvault.net/
* Feel free to propose to build the design on top of one of https://themequarry.net/ themes if it will save the design work, will be easier and faster for you

```html
<!DOCTYPE html>
<html lang="en">
<head>
<meta charset="utf-8">
<title>HaiVoyage – Blog</title>
<link href="https://fonts.googleapis.com/css2?family=Source+Sans+3:wght@400;600;700&display=swap" rel="stylesheet">
<style>
:root{
  --bg-deep:#1f5a96;
  --bg-light:#6fa3d8;
  --brand:#1e64a8;
  --brand-dark:#17528c;
  --nav-top:#2a86cf;
  --nav-bottom:#15609f;
  --nav-active:#39a3e6;
  --panel:#2476bd;
  --panel-dark:#1b5d9a;
  --orange:#f07d16;
  --orange-light:#f7a23a;
  --text:#555;
  --line:#d8d8d8;
  --post-bg:#eeeeee;
  --white:#fff;
  --footer:#4a7eb3;
  --footer-bottom:#3f6f9f;
}
*{box-sizing:border-box;margin:0;padding:0}
html,body{width:1003px;height:1200px;overflow:hidden}
body{font-family:"Source Sans 3",sans-serif;color:var(--text);
  background:radial-gradient(ellipse at center,var(--bg-light) 0%,var(--bg-deep) 70%);position:relative}
.page{position:absolute;left:150px;top:0;width:703px;height:1200px;background:var(--white)}
.abs{position:absolute}
/* header */
.logo{left:10px;top:28px;display:flex;align-items:center;gap:8px}
.logo-mark{width:38px;height:38px;border-radius:50%;background:var(--brand)}
.logo-name{font-size:28px;font-weight:700;color:var(--brand);line-height:1}
.logo-url{font-size:9px;color:var(--brand);font-weight:600;margin-top:2px}
.phone{left:382px;top:40px;display:flex;gap:8px;align-items:center}
.phone-num{font-size:17px;font-weight:700;color:var(--brand);line-height:1}
.phone-call{font-size:13px;color:#333}
.account{left:514px;top:14px;font-size:9.5px;color:var(--brand)}
.social{left:606px;top:11px;display:flex;gap:4px}
.social span{width:18px;height:18px;border-radius:3px;display:block}
.search{left:524px;top:55px;width:165px;height:19px;border:1px solid #ccc;border-radius:2px;font-size:7px;color:#999;padding:5px 8px}
/* nav */
.nav{left:0;top:94px;width:703px;height:28px;background:linear-gradient(var(--nav-top),var(--nav-bottom));display:flex}
.nav a{color:#fff;font-size:8.5px;font-weight:700;text-decoration:none;height:28px;line-height:28px;padding:0 19px;border-right:1px solid rgba(0,0,0,.15)}
.nav a.active{background:var(--nav-active);padding:0 27px}
/* sidebar */
.finder{left:16px;top:138px;width:207px;height:292px;background:var(--panel);border:2px solid var(--panel-dark);border-radius:2px;color:#e3efff}
.finder h2{font-size:18px;font-weight:400;color:#fff;padding:12px 0 6px 18px;border-bottom:1px solid rgba(255,255,255,.2)}
.label{font-size:9.5px;position:absolute}
.select{position:absolute;height:19px;background:linear-gradient(#fafafa,#dcdcdc);border-radius:2px;font-size:7.5px;color:#333;padding:5px 7px}
.select::after{content:"";position:absolute;right:0;top:0;width:16px;height:19px;border-left:1px solid #bbb}
.btn-orange{background:linear-gradient(var(--orange-light),var(--orange));color:#fff;border-radius:2px;text-align:center;font-weight:600}
.newsletter{left:16px;top:449px;width:207px;height:248px;background:linear-gradient(var(--panel),var(--panel-dark));border:2px solid var(--panel-dark);color:#fff}
.photo{background:linear-gradient(135deg,#7fc4e6,#d9c7a8)}
/* main */
.crumbs{left:247px;top:139px;font-size:8.5px;color:var(--brand)}
.title{left:242px;top:172px;font-size:13px;font-weight:700;color:var(--brand)}
.back{left:525px;top:162px;width:162px;height:30px;line-height:30px;font-size:11px}
.post{left:243px;top:204px;width:444px;height:682px;background:var(--post-bg);border:1px solid #ddd}
.post-head{left:17px;top:18px;width:412px;height:25px;border-bottom:1px solid var(--line);display:flex;justify-content:space-between;align-items:center;line-height:1}
.post-title{font-size:9.5px;font-weight:700;color:var(--brand)}
.meta{font-size:7px;color:var(--orange);font-weight:600}
.subhead{font-size:11px;color:var(--orange)}
.copy{font-size:7px;line-height:12.8px;color:#555}
.framed{border:4px solid #fff;box-shadow:0 0 0 1px #ddd}
/* partners */
.partners-title{left:13px;top:906px;font-size:13px;font-weight:700;color:var(--brand)}
.arrows{left:657px;top:907px;display:flex;gap:2px}
.arrows span{width:13px;height:13px;background:#ddd;display:flex;align-items:center;justify-content:center}
.partners{left:14px;top:932px;display:flex;gap:10px}
.partner{width:104px;height:52px;border:1px solid #ddd;display:flex;align-items:center;justify-content:center}
.partner i{display:block;width:62px;height:16px;border-radius:3px;opacity:.8}
/* footer */
.footer{left:0;top:1002px;width:703px;height:160px;background:var(--footer);color:#fff}
.footer h4{font-size:11.5px;font-weight:600}
.footer ul{list-style:none;font-size:7px;line-height:15.7px;margin-top:6px}
.foot-bottom{left:0;top:1162px;width:703px;height:38px;background:var(--footer-bottom);color:#fff;font-size:7px;text-align:center;line-height:36px}
</style>
</head>
<body>
<div class="page">
  <header>
    <div class="abs logo">
      <span class="logo-mark"></span>
      <div><div class="logo-name">HaiVoyage</div><div class="logo-url">www.haivoyage.com</div></div>
    </div>
    <div class="abs phone">
      <svg width="26" height="26" viewBox="0 0 26 26"><circle cx="13" cy="13" r="12" fill="none" stroke="#999" stroke-width="1.5"/><path d="M9 7c-2 2-1 6 2 9s7 4 9 2l-2-3-2 1c-2-1-4-3-5-5l1-2z" fill="#888"/></svg>
      <div><div class="phone-num">400 818 218</div><div class="phone-call">Call Us Today!</div></div>
    </div>
    <div class="abs account">Sign in &nbsp;|&nbsp; Signup</div>
    <div class="abs social"><span style="background:#e2322b"></span><span style="background:#33a6d8"></span><span style="background:#f39a1c"></span><span style="background:#d9363e"></span></div>
    <div class="abs search">SEARCH :</div>
    <nav class="abs nav">
      <a class="active">HOME</a><a>DESTINATIONS</a><a>CRUISE LINES</a><a>CRUISE INFO</a><a>DEALS</a><a>ONLINE BOOKING</a><a>CONTACT US</a><a style="border:0">BLOG</a>
    </nav>
  </header>

  <aside class="abs finder">
    <h2>Find Your Cruise</h2>
    <span class="label" style="left:16px;top:48px">Destination</span>
    <div class="select" style="left:16px;top:62px;width:171px">Destination name</div>
    <span class="label" style="left:17px;top:86px">Length</span>
    <span class="label" style="left:110px;top:86px">Month</span>
    <div class="select" style="left:16px;top:100px;width:78px">Length Area</div>
    <div class="select" style="left:110px;top:100px;width:77px"></div>
    <span class="label" style="left:15px;top:126px">Cruise Lines</span>
    <div class="select" style="left:16px;top:140px;width:171px">Any Cruise line</div>
    <span class="label" style="left:15px;top:170px;font-size:11px;color:#fff">Number of Travelers</span>
    <span class="label" style="left:16px;top:190px">Age 25+</span>
    <span class="label" style="left:109px;top:190px">Age 0 to 24</span>
    <div class="select" style="left:16px;top:203px;width:77px">5</div>
    <div class="select" style="left:110px;top:203px;width:77px">0</div>
    <span class="label" style="left:16px;top:229px;font-size:7.5px"><span style="display:inline-block;width:9px;height:9px;background:#dfe8f2;vertical-align:-1px;margin-right:3px"></span>Check for senior rates</span>
    <div class="abs btn-orange" style="left:16px;top:246px;width:175px;height:28px;line-height:28px;font-size:12px">Search Cruises</div>
  </aside>

  <aside class="abs newsletter">
    <div class="abs photo" role="img" aria-label="Senior couple relaxing in deck chairs by a pool" style="left:9px;top:11px;width:185px;height:111px;border:5px solid #fff"></div>
    <div class="abs" style="left:16px;top:131px;font-size:11px;font-weight:700">Cruise Deals Newsletter</div>
    <div class="abs" style="left:16px;top:150px;font-size:7px">Subscribe to the best Cruise deals Now!</div>
    <div class="abs" style="left:16px;top:169px;width:179px;height:19px;background:#fff;border-radius:2px;font-size:7.5px;color:#999;padding:4px 40px">Email :</div>
    <div class="abs" style="left:17px;top:198px;width:73px;height:19px;background:#0f3c6a;font-size:8px;text-align:center;line-height:19px">Subscribe</div>
    <div class="abs" style="left:19px;top:228px;font-size:8.5px">Contest Rules</div>
  </aside>

  <main>
    <div class="abs crumbs">HOME &nbsp;›&nbsp; BREADCRUMBS</div>
    <h1 class="abs title">BLOG</h1>
    <div class="abs btn-orange back">« BACK TO ALL POSTS</div>

    <article class="abs post">
      <div class="abs post-head"><span class="post-title">LOREM IPSUM IS SIMPLY DUMMY</span><span class="meta">LENA MARSH &nbsp;&nbsp;|&nbsp;&nbsp; POSTED ON 20 JUN 2013</span></div>
      <div class="abs photo" role="img" aria-label="Couple walking through a historic European square" style="left:17px;top:51px;width:412px;height:176px;background:linear-gradient(135deg,#b9aa94,#8a8f99 60%,#6f7c8c)"></div>
      <h3 class="abs subhead" style="left:18px;top:239px;font-weight:400">What services do you provide</h3>
      <p class="abs copy" style="left:19px;top:258px;width:400px">Lorem Ipsum is simply dummy text of the printing and typesetting industry. Lorem Ipsum has been the industry's standard dummy text ever since the 1500s, when an unknown printer took a galley of type and scrambled it to make a type specimen book. It has survived not only five centuries, but also the leap into electronic typesetting, remaining essentially unchanged. It was popularised in the 1960s with the release of Lettrex sheets containing Lorem Ipsum passages, and more recently with desktop publishing software like Quillby PageStudio including versions of Lorem Ipsum.Lorem Ipsum is simply dummy text of the printing and typesetting industry. Lorem Ipsum has been the industry's standard dummy text ever since the 1500s, when an unknown printer took a galley of type and scrambled it to make a type specimen book. It has survived not only five centuries, but also the leap into electronic typesetting, remaining essentially unchanged. It was popularised in the 1960s with the release.</p>
      <p class="abs copy" style="left:19px;top:387px;width:400px">Lorem Ipsum is simply dummy text of the printing and typesetting industry. Lorem Ipsum has been the industry's standard dummy text ever since the 1500s, when an unknown printer took a galley of type and scrambled it to make a type specimen book. It has survived not only five centuries, but also the leap into electronic typesetting, remaining essentially unchanged. It was popularised in the 1960s.</p>
      <div class="abs framed photo" role="img" aria-label="Happy family of four outdoors under a blue sky" style="left:21px;top:451px;width:200px;height:148px;background:linear-gradient(180deg,#5d9ad4,#c9a07a)"></div>
      <p class="abs copy" style="left:238px;top:453px;width:192px">Lorem Ipsum is simply dummy text of the printing and typesetting industry. Lorem Ipsum has been the industry's standard dummy text ever since the 1500s, when an unknown printer took a galley of type and scrambled it to make a type specimen book. It has survived not only five centuries, but also the leap into electronic typesetting, remaining essentially unchanged. It was popularised in the 1960s.of type and scrambled it to make a type specimen book. It has survived not only five centuries, but also the leap into electronic typesetting, remaining essentially unchanged. It was popularised in the 1960s.</p>
      <p class="abs copy" style="left:22px;top:612px;width:410px">Lorem Ipsum is simply dummy text of the printing and typesetting industry. Lorem Ipsum has been the industry's standard dummy text ever since the 1500s, when an unknown printer took a galley of type and scrambled it to make a type specimen book. It has survived not only five centuries, but also the leap into electronic typesetting, remaining essentially unchanged. It was popularised in the 1960s.</p>
    </article>
  </main>

  <section>
    <h2 class="abs partners-title">OUR RELIABLE PARTNERS</h2>
    <div class="abs arrows"><span><svg width="6" height="8"><path d="M5 0L1 4l4 4" stroke="#fff" fill="none"/></svg></span><span><svg width="6" height="8"><path d="M1 0l4 4-4 4" stroke="#fff" fill="none"/></svg></span></div>
    <div class="abs partners">
      <div class="partner"><i style="background:#b8282c"></i></div>
      <div class="partner"><i style="background:#1f4fa0"></i></div>
      <div class="partner"><i style="background:#2e4e78"></i></div>
      <div class="partner"><i style="background:#f09a2a"></i></div>
      <div class="partner"><i style="background:#3a9ad6;border-radius:50%;width:20px;height:20px"></i></div>
      <div class="partner"><i style="background:#2b7fcf"></i></div>
    </div>
  </section>

  <footer class="abs footer">
    <div class="abs" style="left:23px;top:22px"><h4>Useful Pages</h4><ul><li>About Us</li><li>Contact us</li><li>Blog</li><li>FAQ</li><li>Terms of Service</li><li>Payment info</li><li>Reward Points</li></ul></div>
    <div class="abs" style="left:160px;top:22px"><h4>Cruise Infov</h4><ul><li>Cruise news</li><li>Visa</li><li>Honeymoon cruises</li><li>Firsttime on a Cruise</li></ul></div>
    <div class="abs" style="left:291px;top:26px"><h4>About haivoyage.com</h4></div>
    <div class="abs" style="left:291px;top:53px;width:71px;height:71px;background:#fff;display:flex;flex-direction:column;align-items:center;justify-content:center;gap:4px">
      <span style="width:26px;height:26px;border-radius:50%;background:var(--brand)"></span>
      <span style="font-size:8px;font-weight:700;color:var(--brand)">HaiVoyage</span>
    </div>
    <p class="abs" style="left:376px;top:60px;width:80px;font-size:8.5px;line-height:13px">We're the most advanced cruise booking providr in china.</p>
    <div class="abs" style="left:506px;top:26px;font-size:9px;line-height:13.5px">
      <h4 style="margin-bottom:6px">Contact Us</h4>
      Brightwave Studio, Pte Ltd<br>Harbor Plaza x118, Coral Ave 2.1<br>Kelapa 20417 Indonesia
      <div style="margin-top:6px;font-size:8.5px">☏&nbsp; (555) 014-2290 - (555) 014-7731</div>
      <div style="margin-top:4px;font-size:8.5px">✉&nbsp; hello@haivoyage.com</div>
    </div>
  </footer>
  <div class="abs foot-bottom">© 2013. haivoyage. All rights reserved.</div>
</div>
</body>
</html>
```